Clearvantix Brochure Print & Web

Hi,

We're looking for a really attractive, professional brochure design for our services.

The design will be used across multiple lines so should be fairly extensible with main design elements that flow throughout. Ideally, it will be 4 pages. A cover page that is primarily graphic design with some very short text bullet points followed by 2 inside pages with the bulk of the messaging and a back page with a comparison table and light explanatory text. In a perfect world, the two inside pages would be designed so that they could also stand on their own as a front and back of a single sheet in some circumstances.

I've attached our logo as well as a current version of a brochure. You can see our website at www.clearvantix-example.com for additional ideas.

Feel free to primarily use Lorum Ipsum text. There should be graphic elements that convey as much as possible, and space for several customer testimonials. Obviously there will be text but we generally prefer to communicate with headlines, short paragraphs, and bullet points.

Our primary colors are the Blue and Orange that you see on the logo.

This is our first contest so please let me know if you need more information

Target Market(s)

Corporate Customers

Industry/Entity Type

It Professional

Font styles to use
Sans Serif

Colors
f78f20
0455a3

Requirements
Must have
• Designed for 8.5 x 11 (either portrait or landscape is ok)
Nice to have
• We generally prefer full to see the use of full bleed graphics. If you do that, please make sure to include enough bleed so that we can send the document to be printed.

```html
<!DOCTYPE html>
<html lang="en">
<head>
<meta charset="utf-8">
<title>Clearvantix Brochure</title>
<link rel="stylesheet" href="https://fonts.googleapis.com/css2?family=Arimo:wght@400;700&family=Tinos:ital@1&display=swap">
<style>
  :root {
    --brand-blue: #0455a3;
    --brand-orange: #f78f20;
    --deep-blue: #0a55a8;
    --bullet-blue: #1560b0;
    --frame-green: #8db33a;
    --lead-green: #6db32a;
    --lime: #8dc63f;
    --gold: #f2c81a;
    --ink: #111;
    --paper: #fff;
    --sans: "Arimo", Arial, sans-serif;
    --serif: "Tinos", "Times New Roman", serif;
  }
  * { box-sizing: border-box; margin: 0; padding: 0; }
  html, body { width: 1200px; height: 1000px; overflow: hidden; background: var(--paper); font-family: var(--sans); }
  .canvas { position: relative; width: 1200px; height: 1000px; }
  .abs { position: absolute; }

  .sheet { position: absolute; background: var(--paper); overflow: hidden; box-shadow: 2px 4px 10px rgba(0,0,0,.35); }
  .cover { left: 5px; top: 10px; width: 697px; height: 450px; }
  .spread { left: 490px; top: 528px; width: 695px; height: 450px; }

  .wordmark { display: flex; align-items: center; gap: 6px; font-weight: 700; color: var(--brand-blue); letter-spacing: -.3px; white-space: nowrap; }
  .wordmark .mark { background: var(--brand-orange); }

  /* cover */
  .cover-bars { left: 0; top: 0; }
  .cover-frame { left: 35px; top: 87px; width: 260px; height: 296px; border: 1.5px solid var(--frame-green); border-radius: 12px; }
  .bulb-art { left: 188px; top: 8px; width: 312px; height: 442px; border-radius: 22px 22px 0 0;
    background: linear-gradient(to bottom, #eaf2fc 0%, #f7fafe 40%, #dbe8f8 76%, #f6d45a 88%, #f0b81e 100%); }
  .cover-bullets { left: 539px; top: 188px; list-style: none; font-size: 11px; line-height: 16.6px; color: var(--bullet-blue); }
  .cover-url { left: 20px; top: 430px; font-size: 8.5px; color: var(--brand-blue); }
  .cover-chart { left: 427px; top: 365px; }

  .label { position: absolute; font-size: 20px; color: var(--ink); }

  /* spread */
  .page-right { left: 347px; top: 0; width: 348px; height: 450px; background: var(--deep-blue); }
  .lead { font-size: 14px; font-weight: 400; color: var(--lead-green); }
  .intro-art { left: 0; top: 105px; width: 80px; height: 120px; background: linear-gradient(to bottom, #e4eefa, #f3f7fc 70%, #f6e6b0); }
  .intro-panel { left: 78px; top: 105px; width: 255px; height: 100px; background: linear-gradient(135deg, #eef1f6, #f7f9fb); }
  .intro-text { left: 98px; top: 117px; width: 228px; text-align: center; font-size: 9.6px; line-height: 12.2px; color: var(--brand-orange); }
  .heading { font-size: 11.5px; font-weight: 400; color: var(--brand-orange); }
  .body-copy { font-size: 6.6px; line-height: 8.2px; color: var(--ink); }
  .on-blue { color: var(--paper); }
  .quote-box { display: flex; align-items: center; justify-content: center; background: var(--brand-orange); color: var(--paper); font-size: 11px; border-radius: 12px; }
  .badge { background: var(--paper); border: 1.5px solid var(--brand-orange); border-radius: 10px; }
  .wrap-gap-l { float: left; width: 0; }
  .wrap-hole-l { float: left; clear: left; }
  .wrap-gap-r { float: right; width: 0; }
  .wrap-hole-r { float: right; clear: right; }
  .green-line { font-size: 13px; color: var(--lime); white-space: nowrap; }
  .gold-quote { font-family: var(--serif); font-style: italic; font-size: 12px; line-height: 17px; color: var(--gold); text-align: right; }
  .faint-bulb { left: 625px; top: 312px; width: 65px; height: 130px; border-radius: 30px 30px 8px 8px; background: linear-gradient(to bottom, rgba(200,225,250,.35), rgba(120,170,230,.18)); }
</style>
</head>
<body>
<main class="canvas">

  <section class="sheet cover" aria-label="Cover and back page">
    <svg class="abs cover-bars" width="350" height="85" aria-hidden="true">
      <defs>
        <linearGradient id="barFade" x1="0" y1="0" x2="0" y2="1">
          <stop offset="0" stop-color="#f78f20"/><stop offset="1" stop-color="#f9b560"/>
        </linearGradient>
      </defs>
      <g fill="url(#barFade)">
        <rect x="0" y="0" width="19" height="80"/><rect x="21" y="0" width="19" height="55"/>
        <rect x="42" y="0" width="19" height="34"/><rect x="63" y="0" width="19" height="52"/>
        <rect x="84" y="0" width="19" height="15"/><rect x="105" y="0" width="19" height="45"/>
        <rect x="126" y="0" width="19" height="70"/><rect x="147" y="0" width="19" height="60"/>
        <rect x="168" y="0" width="19" height="85"/><rect x="189" y="0" width="19" height="40"/>
        <rect x="210" y="0" width="19" height="28"/><rect x="231" y="0" width="19" height="50"/>
        <rect x="252" y="0" width="19" height="20"/><rect x="273" y="0" width="19" height="38"/>
        <rect x="294" y="0" width="19" height="55"/><rect x="315" y="0" width="19" height="30"/>
        <rect x="336" y="0" width="14" height="18"/>
      </g>
    </svg>
    <div class="abs cover-frame"></div>
    <div class="abs bulb-art" role="img" aria-label="Large glowing light bulb illustration with a gold base"></div>

    <div class="abs wordmark" style="left:478px;top:22px;font-size:25px;">
      <span class="mark" style="width:30px;height:30px;"></span>clearvantix
    </div>

    <ul class="abs cover-bullets">
      <li>Bullet point 1. Some text here</li>
      <li>Bullet point 2. Some text here</li>
      <li>Something else comes here</li>
      <li>Bullet point 3</li>
      <li>Bullet point 3</li>
    </ul>

    <div class="abs wordmark" style="left:17px;top:400px;font-size:14px;">
      <span class="mark" style="width:16px;height:16px;"></span>clearvantix
    </div>
    <p class="abs cover-url">www.clearvantix-example.com</p>

    <svg class="abs cover-chart" width="270" height="85" aria-hidden="true">
      <g fill="#0455a3">
        <rect x="0" y="13" width="19" height="72"/><rect x="21" y="23" width="19" height="62"/>
        <rect x="42" y="52" width="19" height="33"/><rect x="63" y="67" width="19" height="18"/>
        <rect x="84" y="28" width="19" height="57"/><rect x="105" y="36" width="19" height="49"/>
        <rect x="126" y="15" width="19" height="70"/><rect x="147" y="0" width="19" height="85"/>
        <rect x="168" y="43" width="19" height="42"/><rect x="189" y="53" width="19" height="32"/>
        <rect x="210" y="30" width="19" height="55"/><rect x="231" y="57" width="19" height="28"/>
        <rect x="252" y="47" width="18" height="38"/>
      </g>
    </svg>
  </section>

  <svg class="abs" style="left:0;top:0;" width="1200" height="1000" aria-hidden="true">
    <g fill="#8da23a">
      <polygon points="738,240 756,228 756,236 785,236 785,244 756,244 756,252"/>
      <polygon points="185,498 173,516 181,516 181,546 189,546 189,516 197,516"/>
      <polygon points="1045,507 1033,489 1041,489 1041,458 1049,458 1049,489 1057,489"/>
      <polygon points="470,796 452,784 452,792 421,792 421,800 452,800 452,808"/>
    </g>
  </svg>
  <span class="label" style="left:812px;top:228px;">Front</span>
  <span class="label" style="left:153px;top:563px;">Back</span>
  <span class="label" style="left:1012px;top:420px;">Page3</span>
  <span class="label" style="left:337px;top:781px;">Page2</span>

  <section class="sheet spread" aria-label="Inside pages">
    <div class="abs page-right"></div>
    <svg class="abs" style="left:0;top:0;" width="695" height="90" aria-hidden="true">
      <path d="M0 0 H347 V60 C280 20 150 30 0 42 Z" fill="#0a55a8"/>
      <path d="M55 48 C120 20 250 10 340 28 C250 22 140 30 60 55 Z" fill="#0a55a8"/>
      <path d="M347 34 C430 10 580 20 695 38 V82 C600 60 450 70 347 82 Z" fill="#fff"/>
      <path d="M420 28 C500 14 600 18 690 40 C600 28 500 26 430 34 Z" fill="#0a55a8"/>
    </svg>

    <!-- Page 2 -->
    <div class="abs wordmark" style="left:135px;top:36px;font-size:16px;">
      <span class="mark" style="width:18px;height:18px;"></span>clearvantix
    </div>
    <h2 class="abs lead" style="left:10px;top:80px;">Our channel program is all about you</h2>
    <div class="abs intro-panel"></div>
    <div class="abs intro-art" role="img" aria-label="Soft light bulb illustration"></div>
    <p class="abs intro-text">Some Text comes here. Lorem Ipsum dolor sit amet, consectetur&nbsp; Lorem Ipsum dolor sit amet, consectetu. Some Text comes here. Lorem Ipsum dolor sit amet, consectetur&nbsp; Lorem Ipsum dolor sit amet, consectetu. Some Text comes here. Lorem Ipsum dolor sit amet consectetur Lorem Ipsum dolor sit amet, consectetu</p>

    <div class="abs quote-box" style="left:0;top:224px;width:123px;height:81px;border-radius:0 12px 12px 0;">quote</div>
    <h3 class="abs heading" style="left:131px;top:221px;">Heading</h3>
    <div class="abs body-copy" style="left:131px;top:236px;width:212px;">
      <span class="wrap-gap-l" style="height:50px;"></span><span class="wrap-hole-l" style="width:38px;height:50px;"></span>
      Lorem ipsum dolor sit amet, consectetur adipiscing elit, sed do eiusmod tempor incididunt ut labore et dolore magna aliqua. Ut enim ad minim veniam, quis nostrud exercitation ullamco laboris nisi ut aliquip ex ea commodo consequat. Duis aute irure dolor in reprehend in voluptate velit esse cillum dolore eu fugiat nulla pariatur. Excepteur sint occaecat cupidatat non proident, sunt in culpa qui officia deserunt mollit anim id est laborum. Lorem ipsum dolor sit amet, consectetur adipiscing elit, sed do eiusmod tempor incidid ut labore et dolore magna aliqua. Ut enimad minim venia, quis nostrud exercitation ullamco laboris nisi ut aliquip ex ea commodo consequat
    </div>
    <div class="abs badge" style="left:112px;top:288px;width:52px;height:42px;"></div>

    <h3 class="abs heading" style="left:5px;top:331px;">Heading</h3>
    <div class="abs body-copy" style="left:5px;top:346px;width:205px;">
      <span class="wrap-gap-r" style="height:50px;"></span><span class="wrap-hole-r" style="width:40px;height:50px;"></span>
      Lorem ipsum dolor sit amet, consectetur adipiscing elit, sed do sed eiusmod tempor incididunt ut labore et dolore magna aliqua. Ut ad minim veniam, quis nostrud exercitation ullamco laboris nisi ut aliquip ex ea commodo consequat. Duis aute irure dolor in repre in voluptate velit esse cillum dolore eu fugiat nulla pariatur. Excepte sint occaecat cupidatat non proident, sunt in culpa qui officia deser mollit anim id est laborum. Lorem ipsum dolor sit amet, consectetur adipiscing elit, sed do eiusmod tempor in ut labore et dolore magna aliqua. Ut enimad minim ve quis nostrud exercitation ullamco laboris nisi ut aliquip.
    </div>
    <div class="abs quote-box" style="left:215px;top:330px;width:127px;height:82px;">quote</div>
    <div class="abs badge" style="left:176px;top:400px;width:52px;height:42px;"></div>

    <!-- Page 3 -->
    <div class="abs wordmark" style="left:422px;top:40px;font-size:16px;">
      <span class="mark" style="width:18px;height:18px;"></span>clearvantix
    </div>
    <h3 class="abs heading" style="left:353px;top:86px;">Heading</h3>
    <div class="abs body-copy on-blue" style="left:353px;top:101px;width:212px;">
      <span class="wrap-gap-r" style="height:50px;"></span><span class="wrap-hole-r" style="width:40px;height:50px;"></span>
      Lorem ipsum dolor sit amet, consectetur adipiscing elit, sed do eiusmod tempor incididunt ut labore et dolore magna aliqua. Ut enim ad minim veniam, quis nostrud exercitation ullamco laboris nisi ut aliquip ex ea commodo consequat. Duis aute irure dolor in reprehend in voluptate velit esse cillum dolore eu fugiat nulla pariatur. Excepteur sint occaecat cupidatat non proident, sunt in culpa qui officia deserunt mollit anim id est laborum. Lorem ipsum dolor sit amet, consectetur adipiscing elit, sed do eiusmod tempor incidi ut labore et dolore magna aliqua. Ut enimad minim venia, quis nostrud exercitation ullamco laboris nisi ut aliquip.
    </div>
    <div class="abs quote-box" style="left:567px;top:89px;width:128px;height:83px;border-radius:12px 0 0 12px;">quote</div>
    <div class="abs badge" style="left:528px;top:152px;width:52px;height:42px;"></div>

    <h3 class="abs heading" style="left:485px;top:193px;">Heading</h3>
    <div class="abs body-copy on-blue" style="left:485px;top:208px;width:208px;">
      <span class="wrap-gap-l" style="height:50px;"></span><span class="wrap-hole-l" style="width:36px;height:50px;"></span>
      Lorem ipsum dolor sit amet, consectetur adipiscing elit, sed do eiusmod tempor incididunt ut labore et dolore magna aliqua. Ut enim ad minim veniam, quis nostrud exercitation ullamco laboris nisi ut aliquip ex ea commodo consequat. Duis aute irure dolor in reprehe in voluptate velit esse cillum dolore eu fugiat nulla pariatur. Excepte sint occaecat cupidatat non proident, sunt in culpa qui officia deseru mollit anim id est laborum. Lorem ipsum dolor sit amet, consectetur adipiscing elit, sed do eiusmod tempor inci ut labore et dolore magna aliqua. Ut enimad minim ven quis nostrud exercitation ullamco laboris nisi ut aliquip ex ea commodo consequat
    </div>
    <div class="abs quote-box" style="left:352px;top:197px;width:126px;height:81px;">quote</div>
    <div class="abs badge" style="left:466px;top:260px;width:52px;height:42px;"></div>

    <p class="abs green-line" style="left:358px;top:318px;">Lorem Ipsum dolor sit amet, consectetu</p>
    <div class="abs faint-bulb" role="img" aria-label="Faint light bulb illustration"></div>
    <p class="abs gold-quote" style="left:355px;top:348px;width:250px;">Some Text comes here. Lorem Ipsum dolor sit amet,<br>consectetu&nbsp; Lorem Ipsum dolor sit amet,<br>consectetu</p>
  </section>

</main>
</body>
</html>
```